RWM Bricklaying business card

i need a business card designed for my bricklaying company.
I was also hoping to get a logo drawn up so i can put it on some t-shirts.
You can use any style or colours just as long as it lloks good. thanks Dalton

Industry/Entity Type

Business

Contact Information for Business Card

Dalton Briggs
RWM Bricklaying
0461937205
Any type of brick/blockwork
No job too small

```html
<!DOCTYPE html>
<html lang="en">
<head>
<meta charset="utf-8">
<title>RWM Bricklaying – Business Card</title>
<link rel="stylesheet" href="https://fonts.googleapis.com/css2?family=Crimson+Text:wght@400&display=swap">
<style>
  :root {
    --backdrop: #e9e8e6;
    --brick: #a55a40;
    --card-white: #f1f1ef;
    --ink: #1c1c1c;
    --ink-soft: #2e2e2e;
    --logo-white: #f4f1ee;
  }
  * { margin: 0; padding: 0; box-sizing: border-box; }
  html, body {
    width: 1200px;
    height: 1000px;
    overflow: hidden;
    background: var(--backdrop);
    font-family: "Crimson Text", Georgia, serif;
  }
  .card {
    position: absolute;
    left: 240px;
    width: 720px;
    height: 411px;
    overflow: hidden;
    box-shadow: 0 2px 10px rgba(0,0,0,0.12);
  }
  .card--back {
    top: 60px;
    background: var(--brick);
  }
  .card--front {
    top: 521px;
    background: var(--brick);
  }
  .front__panel-light {
    position: absolute;
    left: 0; top: 0;
    width: 396px;
    height: 100%;
    background: var(--card-white);
  }
  .wordmark {
    position: absolute;
    color: var(--logo-white);
    font-weight: 400;
    text-transform: uppercase;
    white-space: nowrap;
  }
  .card--back .wordmark {
    left: 150px;
    top: 150px;
    font-size: 40px;
    letter-spacing: 7px;
  }
  .card--front .wordmark {
    left: 430px;
    top: 182px;
    font-size: 22px;
    letter-spacing: 4px;
  }
  .contact__name {
    position: absolute;
    left: 74px;
    top: 92px;
    font-size: 36px;
    color: var(--ink);
    font-weight: 400;
  }
  .contact__phone {
    position: absolute;
    left: 74px;
    top: 146px;
    font-size: 27px;
    color: var(--ink-soft);
    letter-spacing: 1px;
  }
  .tagline {
    position: absolute;
    left: 74px;
    top: 290px;
    width: 300px;
    font-size: 25px;
    line-height: 1.3;
    color: var(--ink);
  }
  .tagline span { display: block; white-space: nowrap; }
</style>
</head>
<body>
  <section class="card card--back" aria-label="Business card back">
    <p class="wordmark">RWM Bricklaying</p>
  </section>

  <section class="card card--front" aria-label="Business card front">
    <div class="front__panel-light"></div>
    <h1 class="contact__name">Dalton Briggs</h1>
    <p class="contact__phone">P: 046- 193- 7205</p>
    <p class="wordmark">RWM Bricklaying</p>
    <p class="tagline"><span>Any type of brick/blockwork</span><span>No job too small</span></p>
  </section>
</body>
</html>
```